Anzeigengestaltung für Vertrieb von Kunststoffgittern
Zielgruppe
Vertrieb von Kunststoffgittern aus eigener Herstellung zur Bodenbefestigung. Einsatz in der Pferdehaltung. Böden von Paddocks und Ausläufen, Reitplätze, Reithallen, Führanlagen, Roundpen. Parkplatzbefestigung, Weidewege Freß- und Tränkplätze, Offenställe.
Wir benötigen eine neue Anzeige in diversen Pferdezeitschriften. Sie sollte ansprechend, mit hohem Wiedererkennunswert sein
Aufgabenstellung
Anzeige sollte für die Größe: 1/4 Seite mit Satzspiegel 43 x 270 mm, längs und 184 x 67 mm quer passen.
Die Anzeige sollte klar und ansprechend strukturiert sein, sie soll der Imagepflege dienen.
Die Farben Grün / Gelb wie im logo sollten vorherrschen. Ein innovativer Text ist gewünscht.
Zur Information kann die website: www.tarbel-gk.com dienen.
Weitere Fotos können zur Verfügung gestellt werden.

```html
<!DOCTYPE html>
<html lang="de">
<head>
<meta charset="utf-8">
<title>Tarbel GK – Anzeigen</title>
<link href="https://fonts.googleapis.com/css2?family=Encode+Sans+Condensed:wght@400;500&display=swap" rel="stylesheet">
<style>
:root{
  --green:#1f4d36;
  --orange:#e2962c;
  --ink:#2a2a2a;
  --paper:#ffffff;
  --bg:#ffffff;
}
*{margin:0;padding:0;box-sizing:border-box}
html,body{width:1200px;height:989px;overflow:hidden;background:var(--bg)}
body{position:relative;font-family:"Encode Sans Condensed",Arial Narrow,sans-serif;color:var(--ink)}
.ad{position:absolute;background:var(--paper);box-shadow:0 1px 4px rgba(0,0,0,.35);overflow:hidden}
.photo{position:absolute;background:linear-gradient(180deg,#9cc3e6 0%,#c9dff0 14%,#4f7a3a 24%,#6f8a55 31%,#5a616a 38%,#2e3238 70%,#1d2024 100%)}
.photo.wide{background:linear-gradient(180deg,#a7c9e8 0%,#cfe1ef 18%,#5d8442 30%,#7a8a6a 40%,#4d535b 50%,#2a2e34 100%)}
.brand{position:absolute;color:var(--green);font-weight:500;letter-spacing:.5px;white-space:nowrap;display:flex;align-items:center;gap:6px}
.headline{position:absolute;color:var(--ink);font-weight:400}
.offer{position:absolute;color:var(--orange);font-size:11px;line-height:19.5px}
.band{position:absolute;background:var(--green);color:#fff}
.claim{font-weight:500;text-transform:uppercase;line-height:1.08;white-space:nowrap}
.cta{position:absolute;background:#fff;color:var(--orange);border:2px solid #fff;outline:2px solid var(--green);outline-offset:-5px;line-height:1.05}
.contact{color:#fff;font-size:14px;line-height:22px;white-space:nowrap}
.contact svg{width:13px;height:13px;vertical-align:-1px;fill:#fff;margin-right:3px}
.center{text-align:center}
.right{text-align:right}
</style>
</head>
<body>

<!-- Narrow vertical ad A -->
<section class="ad" style="left:26px;top:5px;width:156px;height:981px">
  <div class="brand" style="left:12px;top:18px;font-size:24px">Tarbel GK</div>
  <p class="headline center" style="left:13px;top:72px;width:130px;font-size:17px;line-height:23px">Mit uns ist Ihr Boden ideal befestigt – für alle Einsatzbereiche!</p>
  <p class="headline center" style="left:8px;top:178px;width:140px;font-size:17px;line-height:23px">Schlamm &amp; Matsch gehören der Vergangenheit an.</p>
  <p class="offer center" style="left:13px;top:275px;width:130px;font-size:11.5px;line-height:18.5px">Wir haben die maßgeschneiderte Lösung für Bodenbefestigung im Pferdesport mit Paddockplatten</p>
  <p class="offer center" style="left:2px;top:378px;width:152px;font-size:11.5px;line-height:18.5px">: Reitplätze aller Art : Reithallen : Trab- und Galopp-Rennbahnen : Round Pen : Paddocks und Ausläufe : Offenställe : Führanlagen : Longierzirkel : Weidewege und Koppelzugänge : Futter- und Tränkplätze : Lagerflächen : Park- und Abstellplätze</p>
  <div class="photo" role="img" aria-label="Foto: Reitplatz mit verlegten schwarzen Kunststoff-Bodengittern vor Birken und Himmel" style="left:0;top:575px;width:156px;height:406px"></div>
  <div class="band" style="left:6px;top:771px;width:144px;height:210px">
    <p class="claim" style="position:absolute;left:9px;top:10px;font-size:18px">Befestigungen<br>mit System</p>
    <div class="cta center" style="left:4px;top:58px;width:136px;height:60px;font-size:21px;padding-top:7px">Informieren<br>Sie sich jetzt:</div>
    <p class="contact" style="position:absolute;left:8px;top:130px"><svg viewBox="0 0 24 24"><path d="M6.6 10.8a15 15 0 0 0 6.6 6.6l2.2-2.2a1 1 0 0 1 1-.25 11.4 11.4 0 0 0 3.6.57 1 1 0 0 1 1 1V20a1 1 0 0 1-1 1A17 17 0 0 1 3 4a1 1 0 0 1 1-1h3.5a1 1 0 0 1 1 1c0 1.25.2 2.45.57 3.57a1 1 0 0 1-.25 1z"/></svg>045 21 - 73 18 46<br>info@tarbel-gk.com<br>www.tarbel-gk.com</p>
  </div>
</section>

<!-- Narrow vertical ad B -->
<section class="ad" style="left:243px;top:5px;width:156px;height:981px">
  <div class="brand" style="left:10px;top:16px;font-size:24px">Tarbel GK</div>
  <p class="headline" style="left:9px;top:64px;width:145px;font-size:15.5px;line-height:22px">Mit uns ist Ihr Boden ideal befestigt – für alle Einsatzbereiche! Schlamm &amp; Matsch gehören der Vergangenheit an.</p>
  <p class="offer" style="left:9px;top:200px;width:145px;font-size:11px;line-height:17.6px">Wir haben die maßgeschneiderte Lösung für Bodenbefestigung im Pferdesport mit Paddockplatten : Reitplätze aller Art : Reithallen : Trab- und Galopp-Rennbahnen : Round Pen : Paddocks und Ausläufe : Offenställe : Führanlagen : Longierzirkel : Weidewege und Koppelzugänge : Futter- und Tränkplätze : Lagerflächen : Park- und Abstellplätze</p>
  <div class="photo" role="img" aria-label="Foto: Reitplatz mit verlegten schwarzen Kunststoff-Bodengittern vor Birken und Himmel" style="left:0;top:450px;width:156px;height:531px"></div>
  <div class="band" style="left:4px;top:762px;width:148px;height:219px">
    <p class="claim" style="position:absolute;left:10px;top:13px;font-size:18px">Befestigungen<br>mit System</p>
    <div class="cta center" style="left:4px;top:62px;width:140px;height:68px;font-size:21px;padding-top:10px">Informieren<br>Sie sich jetzt:</div>
    <p class="contact" style="position:absolute;left:9px;top:142px"><svg viewBox="0 0 24 24"><path d="M6.6 10.8a15 15 0 0 0 6.6 6.6l2.2-2.2a1 1 0 0 1 1-.25 11.4 11.4 0 0 0 3.6.57 1 1 0 0 1 1 1V20a1 1 0 0 1-1 1A17 17 0 0 1 3 4a1 1 0 0 1 1-1h3.5a1 1 0 0 1 1 1c0 1.25.2 2.45.57 3.57a1 1 0 0 1-.25 1z"/></svg>045 21 - 73 18 46<br>info@tarbel-gk.com<br>www.tarbel-gk.com</p>
  </div>
</section>

<!-- Horizontal ad A -->
<section class="ad" style="left:486px;top:66px;width:670px;height:243px">
  <div class="photo wide" role="img" aria-label="Foto: Feld mit schwarzen Kunststoff-Bodengittern, ein einzelnes Gitterelement im Vordergrund" style="left:0;top:0;width:330px;height:243px;clip-path:polygon(0 0,178px 0,178px 105px,330px 105px,330px 190px,0 190px,0 243px,0 243px)"></div>
  <div class="photo wide" aria-hidden="true" style="left:0;top:0;width:178px;height:243px"></div>
  <div style="position:absolute;left:76px;top:16px;width:172px;height:46px;background:#fff"></div>
  <div class="brand" style="left:84px;top:22px;font-size:28px">Tarbel GK</div>
  <p class="headline" style="left:244px;top:20px;font-size:15.5px;line-height:22px">Mit uns ist Ihr Boden ideal befestigt – für alle Einsatzbereiche!<br>Schlamm und Matsch gehören der Vergangenheit an.</p>
  <p class="offer right" style="right:13px;top:80px;width:420px;font-size:13.5px;line-height:18px">Wir haben die maßgeschneiderte Lösung für<br>Bodenbefestigung im Pferdesport mit Paddockplatten</p>
  <p class="offer right" style="right:13px;top:120px;width:420px;font-size:10.5px;line-height:16.8px">: Reitplätze aller Art : Reithallen, Trab- und Galopp-Rennbahnen<br>: Round Pen : Paddocks und Ausläufe : Offenställe : Führanlagen<br>: Longierzirkel : Weidewege und Koppelzugänge<br>Futter- und Tränkplätze : Lagerflächen : Park- und Abstellplätze</p>
  <div class="band" style="left:76px;top:191px;width:590px;height:44px">
    <p class="claim right" style="position:absolute;right:6px;top:5px;font-size:16px">Befestigungen mit System</p>
    <p class="contact right" style="position:absolute;right:6px;top:22px;font-size:12.5px"><svg viewBox="0 0 24 24"><path d="M6.6 10.8a15 15 0 0 0 6.6 6.6l2.2-2.2a1 1 0 0 1 1-.25 11.4 11.4 0 0 0 3.6.57 1 1 0 0 1 1 1V20a1 1 0 0 1-1 1A17 17 0 0 1 3 4a1 1 0 0 1 1-1h3.5a1 1 0 0 1 1 1c0 1.25.2 2.45.57 3.57a1 1 0 0 1-.25 1z"/></svg>04521 - 73 18 46 : &nbsp;<svg viewBox="0 0 24 24"><path d="M2 5h20v14H2zm2 2v.5l8 5 8-5V7z"/></svg>info@tarbel-gk.com &nbsp;: &nbsp;www.tarbel-gk.com</p>
  </div>
  <div class="cta" style="left:78px;top:193px;width:98px;height:46px;font-size:16px;padding:6px 0 0 8px">Informieren<br>Sie sich jetzt:</div>
</section>

<!-- Horizontal ad B -->
<section class="ad" style="left:487px;top:383px;width:670px;height:243px">
  <div class="photo wide" role="img" aria-label="Foto: Feld mit schwarzen Kunststoff-Bodengittern, ein einzelnes Gitterelement im Vordergrund" style="left:0;top:0;width:169px;height:243px"></div>
  <div style="position:absolute;left:63px;top:24px;width:164px;height:48px;background:#fff"></div>
  <div class="brand" style="left:71px;top:30px;font-size:29px">Tarbel GK</div>
  <p class="headline" style="left:238px;top:30px;font-size:16px;line-height:22px">Mit uns ist Ihr Boden ideal befestigt – für alle Einsatzbereiche!<br>Schlamm und Matsch gehören der Vergangenheit an.</p>
  <p class="offer right" style="right:17px;top:84px;width:420px;font-size:10.5px;line-height:16.8px">Wir haben die maßgeschneiderte Lösung für Bodenbefestigung<br>im Pferdesport mit Paddockplatten : Reitplätze aller Art : Reithallen<br>Trab- und Galopp-Rennbahnen : Round Pen : Paddocks und Ausläufe<br>Offenställe : Führanlagen : Longierzirkel : Weidewege und Koppelzugänge<br>Futter- und Tränkplätze : Lagerflächen : Park- und Abstellplätze</p>
  <p class="claim right" style="position:absolute;right:17px;top:175px;font-size:17px;color:var(--green)">Befestigungen mit System</p>
  <div class="band" style="left:100px;top:205px;width:566px;height:32px">
    <p class="contact right" style="position:absolute;right:4px;top:5px;font-size:12.5px"><svg viewBox="0 0 24 24"><path d="M6.6 10.8a15 15 0 0 0 6.6 6.6l2.2-2.2a1 1 0 0 1 1-.25 11.4 11.4 0 0 0 3.6.57 1 1 0 0 1 1 1V20a1 1 0 0 1-1 1A17 17 0 0 1 3 4a1 1 0 0 1 1-1h3.5a1 1 0 0 1 1 1c0 1.25.2 2.45.57 3.57a1 1 0 0 1-.25 1z"/></svg>04521 - 73 18 46 : &nbsp;<svg viewBox="0 0 24 24"><path d="M2 5h20v14H2zm2 2v.5l8 5 8-5V7z"/></svg>info@tarbel-gk.com &nbsp;: &nbsp;www.tarbel-gk.com</p>
  </div>
  <div class="cta" style="left:102px;top:205px;width:178px;height:32px;font-size:18px;padding:5px 0 0 12px">Jetzt informieren:</div>
</section>

</body>
</html>
```